Brevick Summit Builders

I own a roofing business Brevickroofing.com and I want to get a Facebook page YouTube Chanel Instagram twitter all the platforms I can add my business to

```html
<!DOCTYPE html>
<html lang="en">
<head>
<meta charset="utf-8">
<title>Brevick Summit Builders – Cover Banner</title>
<link rel="stylesheet" href="https://fonts.googleapis.com/css2?family=Roboto+Condensed:wght@700&family=Open+Sans:wght@400;600&display=swap">
<style>
  :root {
    --page-bg: #eef0f4;
    --navy: #0f2340;
    --red: #ec1c24;
    --white: #ffffff;
    --roof-dark: #5a3d30;
    --roof-light: #a57e67;
    --body-text: #e3e8ef;
  }
  html, body {
    margin: 0;
    padding: 0;
    width: 1200px;
    height: 1200px;
    overflow: hidden;
    background: var(--page-bg);
  }
  .cover-banner {
    position: absolute;
    left: 48px;
    top: 390px;
    width: 1104px;
    height: 420px;
    overflow: hidden;
    background: var(--navy);
  }
  .banner-shapes, .roof-photo {
    position: absolute;
    left: 0;
    top: 0;
    width: 1104px;
    height: 420px;
  }
  .brand-tag {
    position: absolute;
    left: 968px;
    top: 14px;
    width: 124px;
    display: flex;
    align-items: center;
    gap: 6px;
    font-family: "Open Sans", sans-serif;
    font-weight: 600;
    font-size: 12px;
    line-height: 1.2;
    color: var(--navy);
  }
  .brand-mark {
    flex: none;
    width: 10px;
    height: 10px;
    background: var(--red);
  }
  .headline {
    position: absolute;
    right: 20px;
    top: 138px;
    margin: 0;
    text-align: right;
    font-family: "Roboto Condensed", sans-serif;
    font-weight: 700;
    color: var(--white);
    text-transform: uppercase;
    line-height: 1;
  }
  .headline-main { display: block; font-size: 36px; letter-spacing: 0.2px; }
  .headline-sub { display: block; font-size: 22px; margin-top: 8px; }
  .headline-place { display: block; font-size: 32px; margin-top: 8px; }
  .intro {
    position: absolute;
    left: 675px;
    top: 262px;
    width: 395px;
    margin: 0;
    text-align: center;
    font-family: "Open Sans", sans-serif;
    font-size: 14.5px;
    line-height: 19px;
    color: var(--body-text);
  }
  .divider {
    position: absolute;
    left: 675px;
    top: 331px;
    width: 429px;
    height: 1px;
    background: var(--body-text);
  }
  .contact-list {
    position: absolute;
    left: 675px;
    top: 348px;
    width: 429px;
    font-family: "Open Sans", sans-serif;
    font-size: 16px;
    color: var(--white);
    letter-spacing: 0.4px;
  }
  .contact-row {
    display: flex;
    justify-content: center;
    gap: 30px;
    margin-bottom: 12px;
  }
  .contact-item {
    display: inline-flex;
    align-items: center;
    gap: 6px;
    white-space: nowrap;
  }
  .contact-icon { width: 13px; height: 13px; fill: var(--white); }
</style>
</head>
<body>
  <section class="cover-banner">
    <svg class="roof-photo" viewBox="0 0 1104 420" role="img" aria-label="Close-up photo of brown clay roof tiles in diagonal rows">
      <defs>
        <linearGradient id="roofTone" x1="0" y1="0" x2="1" y2="1">
          <stop offset="0" stop-color="var(--roof-light)"/>
          <stop offset="0.5" stop-color="#7f5b47"/>
          <stop offset="1" stop-color="var(--roof-dark)"/>
        </linearGradient>
      </defs>
      <polygon points="0,0 576,0 675,420 0,420" fill="url(#roofTone)"/>
    </svg>
    <svg class="banner-shapes" viewBox="0 0 1104 420" aria-hidden="true">
      <polygon points="0,0 93,0 180,420 0,420" fill="var(--red)"/>
      <polygon points="936,0 1104,0 1104,73 955,73" fill="var(--white)"/>
    </svg>

    <div class="brand-tag"><span class="brand-mark"></span><span>Brevick Summit Builders</span></div>

    <h1 class="headline">
      <span class="headline-main">#1 Roof Replacement &amp;</span>
      <span class="headline-sub">Repair Services Contractor</span>
      <span class="headline-place">In Metro St. Louis</span>
    </h1>

    <p class="intro">Brevick Summit Builders has over 14 years experience as a roofing contractor in the Metro St. Louis Region. Trust your home to a local expert in roofing.</p>

    <div class="divider"></div>

    <div class="contact-list">
      <div class="contact-row">
        <span class="contact-item">
          <svg class="contact-icon" viewBox="0 0 24 24"><path d="M6.6 10.8a15.1 15.1 0 0 0 6.6 6.6l2.2-2.2a1 1 0 0 1 1-.25 11.4 11.4 0 0 0 3.6.57 1 1 0 0 1 1 1V20a1 1 0 0 1-1 1A17 17 0 0 1 3 4a1 1 0 0 1 1-1h3.5a1 1 0 0 1 1 1c0 1.25.2 2.45.57 3.57a1 1 0 0 1-.25 1z"/></svg>
          (555) 014-2837
        </span>
        <span class="contact-item">
          <svg class="contact-icon" viewBox="0 0 24 24"><path d="M2 5h20v14H2z M2 5l10 8 10-8" fill="none" stroke="#fff" stroke-width="0"/><path d="M2 5h20L12 12z"/><path d="M2 7l10 7 10-7v12H2z"/></svg>
          brevickroofing@mail.com
        </span>
      </div>
      <div class="contact-row">
        <span class="contact-item">
          <svg class="contact-icon" viewBox="0 0 24 24"><circle cx="12" cy="12" r="10"/><path d="M2 12h20M12 2c3 3 3 17 0 20M12 2c-3 3-3 17 0 20" fill="none" stroke="var(--navy)" stroke-width="1.6"/></svg>
          brevickroofing.com
        </span>
      </div>
    </div>
  </section>
</body>
</html>
```